Sandwich Board and Poster design promoting a medical aesthetic clinic

I am looking for a clean, modern and relaxing design promoting a medical physician-led aesthetic clinic.
Services offered are neuromodulator treatment (Quelvo) and Dermal Fillers.
Logo must be included.
Use the tag line "Refresh your look, revive your spirit."
Address is 204-205 27361 92 Ave, Surrey, V7K 2M4
604-555-0148
email - info@lumawellpine.ca
www.lumawellpine.ca

```html
<!DOCTYPE html>
<html lang="en">
<head>
<meta charset="utf-8">
<title>Lumawell Pine – Poster</title>
<link href="https://fonts.googleapis.com/css2?family=Quicksand:wght@300;700&family=Poppins:wght@400;600&family=Montserrat:wght@500&display=swap" rel="stylesheet">
<style>
  :root{
    --stage:#eeeeee;
    --pink-light:#f7d6e6;
    --pink-mid:#eba9cb;
    --pink-deep:#d06ea5;
    --portrait-tone:#f3c4da;
    --skin:#dc9a9c;
    --skin-deep:#c77f86;
    --hair:#5a2f33;
    --ink:#141414;
    --gold:#d2a92b;
    --white:#ffffff;
    --panel:rgba(92,48,60,.6);
  }
  *{margin:0;padding:0;box-sizing:border-box}
  html,body{width:1200px;height:882px;overflow:hidden;background:var(--stage)}
  .poster{
    position:absolute;left:314px;top:0;width:572px;height:882px;overflow:hidden;
    background:linear-gradient(100deg,var(--pink-light) 0%,var(--pink-mid) 55%,var(--pink-deep) 100%);
  }
  .portraits{
    position:absolute;top:0;height:300px;width:190px;
    background:linear-gradient(180deg,var(--portrait-tone) 0%,rgba(243,196,218,.85) 70%,rgba(243,196,218,0) 100%);
  }
  .portraits--left{left:0;border-bottom-right-radius:60px}
  .portraits--right{right:0;border-bottom-left-radius:60px;
    background:linear-gradient(180deg,#f2bfd6 0%,rgba(236,170,202,.85) 70%,rgba(236,170,202,0) 100%)}
  .treatment-photo{
    position:absolute;left:0;right:0;top:440px;bottom:0;
    border-top-left-radius:40px;border-top-right-radius:40px;
    background:
      linear-gradient(200deg,var(--skin) 0%,var(--skin-deep) 45%,#9a5a60 70%,var(--hair) 100%);
  }
  .brand{
    position:absolute;top:120px;left:0;width:100%;
    display:flex;justify-content:center;align-items:center;gap:12px;
    font-family:'Montserrat',sans-serif;font-weight:500;color:var(--ink);
    font-size:26px;letter-spacing:8px;
  }
  .brand__dot{width:12px;height:12px;border-radius:50%;background:var(--gold)}
  .tagline{
    position:absolute;top:192px;left:0;width:100%;text-align:center;
    font-family:'Quicksand',sans-serif;color:var(--white);
    font-size:68px;line-height:59px;letter-spacing:-1px;
    text-shadow:0 2px 6px rgba(120,60,90,.25);
  }
  .tagline .light{font-weight:300}
  .tagline .bold{font-weight:700}
  .contact{
    position:absolute;left:377px;top:769px;width:178px;height:87px;font-style:normal;
    background:var(--panel);border-radius:14px;padding:12px 10px 0 11px;
    font-family:'Poppins',sans-serif;color:var(--white);font-size:12.5px;line-height:15.5px;
  }
  .contact__row{display:flex;align-items:flex-start;gap:5px}
  .contact__row svg{flex:none;margin-top:3px}
  .contact__phone{font-weight:600;font-size:13px}
  .website{
    position:absolute;left:27px;top:844px;display:flex;align-items:center;gap:8px;
    font-family:'Poppins',sans-serif;color:var(--white);font-size:12.5px;
  }
</style>
</head>
<body>
<main class="poster">
  <div class="portraits portraits--left" role="img" aria-label="Faded profile portraits of women"></div>
  <div class="portraits portraits--right" role="img" aria-label="Faded profile portraits of women"></div>
  <div class="treatment-photo" role="img" aria-label="Photo of a woman lying back receiving a cosmetic injection from gloved hands"></div>

  <div class="brand"><span class="brand__dot"></span><span>LUMAWELL PINE</span></div>

  <h1 class="tagline">
    <span class="bold">Refresh</span><br>
    <span class="light">your</span> <span class="bold">look,</span><br>
    <span class="bold">revive</span><br>
    <span class="light">your</span> <span class="bold">spirit.</span>
  </h1>

  <address class="contact">
    <div class="contact__row contact__phone">
      <svg width="9" height="9" viewBox="0 0 10 10"><circle cx="5" cy="5" r="4.3" fill="none" stroke="#d2a92b" stroke-width="1.2"/><path d="M3.4 3c.3 1.6 1.4 3 3.2 3.6" stroke="#d2a92b" stroke-width="1.2" fill="none"/></svg>
      <span>604-555-0148</span>
    </div>
    <div class="contact__row">
      <svg width="9" height="9" viewBox="0 0 10 10"><circle cx="5" cy="5" r="4.3" fill="none" stroke="#d2a92b" stroke-width="1.2"/><rect x="2.8" y="3.6" width="4.4" height="3" fill="none" stroke="#d2a92b" stroke-width=".9"/></svg>
      <span>info@lumawellpine.ca</span>
    </div>
    <div class="contact__row">
      <svg width="9" height="9" viewBox="0 0 10 10"><circle cx="5" cy="5" r="4.3" fill="none" stroke="#d2a92b" stroke-width="1.2"/><circle cx="5" cy="4.4" r="1.3" fill="#d2a92b"/></svg>
      <span>204-205 27361 92 Ave,<br>Surrey, V7K 2M4</span>
    </div>
  </address>

  <div class="website">
    <svg width="10" height="10" viewBox="0 0 10 10"><circle cx="5" cy="5" r="4.3" fill="none" stroke="#fff" stroke-width="1"/><circle cx="5" cy="5" r="2.4" fill="#fff"/></svg>
    <span>www.lumawellpine.ca</span>
  </div>
</main>
</body>
</html>
```